Plakat-Design: Hausmesse Robotik und Cobots
Zielgruppe
High-Tech Engineering aus Euskirchen
Die KW Konstrukteure & Fachservice GmbH mit Sitz in Euskirchen entwickelt moderne Maschinen Robotiklösungen für Kunden in der Region, überregional und bundesweit. Mittelständische Unternehmen und Maschinenbauer, internationale Großkonzerne aus der Konsumgüterindustrie und Hersteller von Maschinen für die weiterverarbeitende Industrie vertrauen KW seit vielen Jahren.
> Maschinenbau
> Automation
> Robotik
> Certified Systemintegrator für Brennwald Mechatronik
Aufgabenstellung
Projektauftrag:
Flyer/Plakat zur Einladung Hausmesse
Format:
> Din A4 PDF zur Einladung der Kunten (digital)
> Werbebanner für E-Mail Signatur
Daten der Messe:
> 18.05.2022 10-17 Uhr
> KW Technik , Lindenhofer Weg 14, 53879 Erlenbrück
> Anmeldeplattform folgt
Motto der Veranstaltung:
> 'Automation - so einfach'
> 'Einfach automatisieren mit Cobots'
> Für Vorschläge gerne offen
Was erwartet Sie:
> Roboter Demos
> Kamerageführte Robotik
> Plug & Play Lösungen
Ausstellerinformationen:
> Bitte unten Platz für Logos der Aussteller vorsehen (derzeit ca. 15)
> Logos können später übermittelt werden
Infomaterial für den Designer:
>> www.kw-technik-beispiel.de
>> www.brennwald-mechatronik-beispiel.de
>> Weitere Bilder sind vorhanden.
>> Farbeschema der PowerPoint nutzen (Vertriebspräsentation_de_KW_21-06-23.pptx)

```html
<!DOCTYPE html>
<html lang="de">
<head>
<meta charset="utf-8">
<title>Hausmesse KW Technik – Automation so einfach</title>
<link href="https://fonts.googleapis.com/css2?family=Exo+2:ital,wght@0,700;1,400;1,600;1,800&family=Noto+Sans:wght@500&display=swap" rel="stylesheet">
<style>
  :root {
    --page: #ffffff;
    --brand-blue: #1e4b9c;
    --logo-blue: #1a4697;
    --ink-dark: #1f1f1f;
    --box-dark: rgba(32, 32, 32, 0.93);
    --white: #ffffff;
    --placeholder: #e1e1e1;
    --footer-grey: #8a8a8a;
    --photo-light: #bfe3f5;
    --photo-mid: #5aa6e0;
    --photo-deep: #2f57b5;
  }
  html, body {
    margin: 0;
    padding: 0;
    width: 768px;
    height: 1200px;
    overflow: hidden;
    background: var(--page);
  }
  body { position: relative; font-family: "Exo 2", sans-serif; }

  /* Poster */
  .poster {
    position: absolute;
    left: 119px; top: 75px;
    width: 552px; height: 779px;
    background: var(--white);
    overflow: hidden;
  }
  .poster-photo {
    position: absolute;
    left: 0; top: 0;
    width: 552px; height: 453px;
    background: linear-gradient(100deg, var(--photo-deep) 0%, var(--photo-mid) 45%, var(--photo-light) 75%, var(--photo-mid) 100%);
  }
  .brand-mark {
    position: absolute;
    right: 35px; top: 130px;
    display: flex; align-items: center; gap: 7px;
    font-family: "Exo 2", sans-serif;
    font-weight: 700;
    font-size: 28px;
    color: var(--logo-blue);
    white-space: nowrap;
  }
  .brand-mark .brand-square {
    width: 16px; height: 16px;
    background: var(--logo-blue);
  }
  .feature {
    position: absolute;
    left: 317px;
    width: 235px;
    background: var(--box-dark);
    color: var(--white);
    font-style: italic;
    font-weight: 600;
    font-size: 22px;
    line-height: 25px;
    box-sizing: border-box;
    padding-left: 16px;
    display: flex; align-items: center;
  }
  .feature-demos { top: 197px; height: 40px; }
  .feature-camera { top: 258px; height: 58px; }
  .feature-plug { top: 338px; height: 58px; }

  .headline-band {
    position: absolute;
    left: 0; top: 453px;
    width: 552px; height: 62px;
    background: var(--brand-blue);
  }
  .headline {
    position: absolute;
    right: 37px; top: 50%;
    transform: translateY(-52%);
    margin: 0;
    color: var(--white);
    font-style: italic;
    font-weight: 800;
    font-size: 41px;
    letter-spacing: -1px;
    white-space: nowrap;
  }
  .date-band {
    position: absolute;
    left: 227px; top: 515px;
    width: 325px; height: 47px;
    background: var(--ink-dark);
  }
  .date {
    position: absolute;
    right: 38px; top: 50%;
    transform: translateY(-52%);
    color: var(--white);
    font-style: italic;
    font-weight: 400;
    font-size: 28px;
    white-space: nowrap;
  }
  .exhibitor-slot {
    position: absolute;
    width: 61px; height: 38px;
    background: var(--placeholder);
  }
  .footer-address {
    position: absolute;
    left: 0; width: 552px;
    top: 746px;
    margin: 0;
    text-align: center;
    font-family: "Noto Sans", sans-serif;
    font-weight: 500;
    font-size: 12px;
    color: var(--footer-grey);
  }

  /* Email signature banner */
  .banner {
    position: absolute;
    left: 77px; top: 983px;
    width: 614px; height: 102px;
    overflow: hidden;
    background: var(--white);
  }
  .banner-photo {
    position: absolute;
    left: 0; top: 0;
    width: 614px; height: 102px;
    background: linear-gradient(100deg, var(--photo-deep) 0%, var(--photo-mid) 45%, var(--photo-light) 100%);
  }
  .banner-headline-band {
    position: absolute;
    left: 201px; top: 0;
    width: 413px; height: 57px;
    background: var(--brand-blue);
  }
  .banner-headline {
    position: absolute;
    right: 18px; top: 50%;
    transform: translateY(-52%);
    margin: 0;
    color: var(--white);
    font-style: italic;
    font-weight: 800;
    font-size: 34px;
    letter-spacing: -0.8px;
    white-space: nowrap;
  }
  .banner-date-band {
    position: absolute;
    left: 328px; top: 57px;
    width: 286px; height: 45px;
    background: #000;
  }
  .banner-date {
    position: absolute;
    right: 22px; top: 50%;
    transform: translateY(-52%);
    color: var(--white);
    font-style: italic;
    font-weight: 400;
    font-size: 25px;
    white-space: nowrap;
  }
</style>
</head>
<body>

<section class="poster">
  <div class="poster-photo" role="img" aria-label="Foto: Cobot-Roboterarm mit kamerageführtem Greifer vor einer blauen Schutzzaun-Zelle"></div>

  <div class="brand-mark"><span class="brand-square"></span>KW Technik</div>

  <div class="feature feature-demos">Roboter Demos</div>
  <div class="feature feature-camera">Kamerageführte<br>Robotik</div>
  <div class="feature feature-plug">Plug &amp; Play<br>Lösungen</div>

  <div class="headline-band"><h1 class="headline">Automation – so einfach</h1></div>
  <div class="date-band"><span class="date">18.05.2022 10-17 Uhr</span></div>

  <div class="exhibitors" aria-label="Platz für Ausstellerlogos">
    <div class="exhibitor-slot" style="left:29px;top:581px"></div>
    <div class="exhibitor-slot" style="left:109px;top:581px"></div>
    <div class="exhibitor-slot" style="left:189px;top:581px"></div>
    <div class="exhibitor-slot" style="left:270px;top:581px"></div>
    <div class="exhibitor-slot" style="left:349px;top:581px"></div>
    <div class="exhibitor-slot" style="left:429px;top:581px"></div>

    <div class="exhibitor-slot" style="left:58px;top:636px"></div>
    <div class="exhibitor-slot" style="left:137px;top:636px"></div>
    <div class="exhibitor-slot" style="left:217px;top:636px"></div>
    <div class="exhibitor-slot" style="left:298px;top:636px"></div>
    <div class="exhibitor-slot" style="left:378px;top:636px"></div>
    <div class="exhibitor-slot" style="left:458px;top:636px"></div>

    <div class="exhibitor-slot" style="left:29px;top:692px"></div>
    <div class="exhibitor-slot" style="left:109px;top:692px"></div>
    <div class="exhibitor-slot" style="left:189px;top:692px"></div>
    <div class="exhibitor-slot" style="left:270px;top:692px"></div>
    <div class="exhibitor-slot" style="left:349px;top:692px"></div>
    <div class="exhibitor-slot" style="left:429px;top:692px"></div>
  </div>

  <p class="footer-address">KW Technik • Lindenhofer Weg 14 • 53879 Erlenbrück</p>
</section>

<section class="banner">
  <div class="banner-photo" role="img" aria-label="Foto: Greifer eines Cobot-Roboterarms mit Kamera vor blauem Hintergrund"></div>
  <div class="banner-headline-band"><h2 class="banner-headline">Automation – so einfach</h2></div>
  <div class="banner-date-band"><span class="banner-date">18.05.2022 10-17 Uhr</span></div>
</section>

</body>
</html>
```